Business Card for Technology Startup

Design a 2-sided business card using the logo provided. We are a digital healthcare platform that provides a mobile app and web UI that helps caregivers, families, and doctors share information and provide better patient outcomes. We use AI and machine learning to help guide patients through their day-to-day life. The final design should communicate stability, peace, comfort, but also align with the image of an AI-driven technology startup.

I'd like the deliverable to by a Photoshop PSD file (with layers) that I can work with in pixlr.com. Should contain the following editable layers:
Name (ex. John Doe)
Title (ex. Founder / CEO)
Email (ex. info@brenvaxa.ai)
Phone (ex. (555) 014-2287)
Website (ex. https://brenvaxa.ai)

```html
<!DOCTYPE html>
<html lang="en">
<head>
<meta charset="utf-8">
<title>Brenvaxa Business Card</title>
<link rel="stylesheet" href="https://fonts.googleapis.com/css2?family=Poppins:wght@400;500;600;700&display=swap">
<style>
  :root {
    --stage: #e9ebed;
    --card-dark: #1c191f;
    --card-light: #f7f7f7;
    --ink: #141414;
    --ink-soft: #2a2a2a;
    --white: #ffffff;
    --accent: #1fb6ee;
    --teal-deep: #0f5f72;
    --teal-mid: #137a8c;
    --aqua-soft: #7dcfe4;
    --aqua-light: #8ee6ec;
  }
  * { box-sizing: border-box; margin: 0; padding: 0; }
  html, body {
    width: 1200px;
    height: 900px;
    overflow: hidden;
    background: var(--stage);
    font-family: "Poppins", sans-serif;
  }
  .stage {
    position: relative;
    width: 1200px;
    height: 900px;
  }
  .card {
    position: absolute;
    left: 250px;
    width: 700px;
    height: 400px;
    border-radius: 4px;
    overflow: hidden;
    box-shadow: 0 10px 30px rgba(0, 0, 0, 0.18);
  }
  .card--back { top: 35px; background: var(--card-dark); }
  .card--front { top: 465px; background: var(--card-light); }

  .brand-shape {
    position: absolute;
    right: 0;
    top: 0;
    width: 300px;
    height: 100%;
    border-top-left-radius: 160px;
    border-bottom-left-radius: 160px;
  }
  .card--back .brand-shape {
    background: linear-gradient(160deg, var(--teal-mid), var(--teal-deep));
  }
  .card--front .brand-shape {
    background: linear-gradient(160deg, var(--aqua-light), var(--aqua-soft));
  }

  .wordmark {
    position: absolute;
    left: 62px;
    top: 88px;
    display: flex;
    align-items: center;
    gap: 12px;
  }
  .wordmark__dot {
    width: 22px;
    height: 22px;
    border-radius: 50%;
    background: var(--accent);
  }
  .wordmark__name {
    font-weight: 600;
    font-size: 44px;
    letter-spacing: 0.5px;
    line-height: 1;
  }
  .card--back .wordmark__name { color: var(--white); }
  .card--front .wordmark__name { color: var(--ink); }

  .person {
    position: absolute;
    left: 62px;
    top: 235px;
    color: var(--ink);
  }
  .person__name { font-weight: 700; font-size: 17px; line-height: 1.3; }
  .person__title { font-weight: 400; font-size: 17px; line-height: 1.3; color: var(--ink-soft); }

  .contact {
    position: absolute;
    left: 62px;
    top: 305px;
    list-style: none;
  }
  .contact__item {
    display: flex;
    align-items: center;
    gap: 10px;
    font-size: 17px;
    line-height: 1.45;
    color: var(--ink);
  }
  .contact__icon { width: 18px; height: 18px; flex: none; }
</style>
</head>
<body>
<main class="stage">

  <section class="card card--back" aria-label="Card back">
    <div class="wordmark">
      <span class="wordmark__dot"></span>
      <span class="wordmark__name">brenvaxa</span>
    </div>
    <div class="brand-shape" role="img" aria-label="Brand decorative shape in deep teal"></div>
  </section>

  <section class="card card--front" aria-label="Card front">
    <div class="wordmark">
      <span class="wordmark__dot"></span>
      <span class="wordmark__name">brenvaxa</span>
    </div>
    <div class="brand-shape" role="img" aria-label="Brand decorative shape in light aqua"></div>

    <div class="person">
      <p class="person__name">John Doe</p>
      <p class="person__title">Founder / CEO</p>
    </div>

    <ul class="contact">
      <li class="contact__item">
        <svg class="contact__icon" viewBox="0 0 18 18" fill="none" stroke="#1fb6ee" stroke-width="1.5">
          <rect x="1" y="1" width="16" height="16" rx="4"/>
          <rect x="4.5" y="5.5" width="9" height="7" rx="1"/>
          <path d="M4.5 6l4.5 3.5L13.5 6"/>
        </svg>
        <span>info@brenvaxa.ai</span>
      </li>
      <li class="contact__item">
        <svg class="contact__icon" viewBox="0 0 18 18" fill="none" stroke="#1fb6ee" stroke-width="1.5">
          <rect x="1" y="1" width="16" height="16" rx="4"/>
          <path d="M5 11.5c0-3 2-5 4-5s4 2 4 5z"/>
          <circle cx="9" cy="10" r="1.2"/>
        </svg>
        <span>(555) 014-2287</span>
      </li>
      <li class="contact__item">
        <svg class="contact__icon" viewBox="0 0 18 18" fill="none" stroke="#1fb6ee" stroke-width="1.5">
          <rect x="1" y="1" width="16" height="16" rx="4"/>
          <circle cx="9" cy="9" r="4.5"/>
          <ellipse cx="9" cy="9" rx="2" ry="4.5"/>
          <path d="M4.5 9h9"/>
        </svg>
        <span>www.brenvaxa.ai</span>
      </li>
    </ul>
  </section>

</main>
</body>
</html>
```